Verpackungen für Parfum-Proben
Besten Dank! Das Team ist begeistert - also bin ich es auch und wir freuen uns schon, unsere Parfum Proben in Zukunft in diesem tollen Design weitergeben zu können! Danke!
Zielgruppe
Hallo allerseits! Wir sind im Direktvertrieb in den Bereichen Parfum & Kosmetik tätig.
Aufgabenstellung
Für unsere Parfum-Proben benötige ich ein ansprechendes, modernes Design.
Das Design muss relativ neutral gehalten werden, da die Blister sowohl für Herren- als auch Damenproben verwendet werden.
Auf Vorder- und Rückseite soll unser Team-Logo (RuchKontor®) sichtbar sein (Vorderseite größer, Rückseite kleiner).
Auf der linken Innenseite sollte Plätz für einen netten Spruch (den ich mir noch überlege) sein.
Auf der Rückseite muss Platz (weißes / helles Feld) für einen Stempel und/oder Aufkleber (Kontaktdaten des Distributors) sein.
Unser Logo ist Lila - Das farbliche Design sollte dazu passen.
Bei Fragen, einfach Nachricht :)
Daten:
Endformat: 133 x 74 mm
Datenformat: 139 x 80 mm
1-teilig, gestanzt, genutet, einseitig geklebt geliefert
Bitte verwenden Sie für positive Schriftstärken mindestens 9pt (ca. 3,17mm) und bei negativen Schriftstärken mindestens 13pt (ca. 4,59mm).
Abmessungen / Druck- / Designvorlage, Logo, etc.: https://dateiwolke.example/ordner/X7KPtrWQ#m4vbeLhNcyrGzzt9_k2w8p

```html
<!DOCTYPE html>
<html lang="de">
<head>
<meta charset="utf-8">
<title>RuchKontor – Probenverpackung, Außen- und Innenseite</title>
<link rel="stylesheet" href="https://fonts.googleapis.com/css2?family=Dancing+Script:wght@500&family=Open+Sans:wght@400&display=swap">
<style>
  :root {
    --stage: #e3e3e3;
    --lavender: #a99cca;
    --violet: #6a55a0;
    --white: #ffffff;
    --quote-text: #f1ecfa;
    --die-line: #e0197d;
  }
  html, body {
    margin: 0;
    padding: 0;
    width: 1200px;
    height: 2330px;
    overflow: hidden;
    background: var(--stage);
  }
  .sheet-stack {
    position: absolute;
    left: 80px;
    top: 529px;
    width: 1040px;
    display: flex;
    flex-direction: column;
    gap: 120px;
  }
  .sheet {
    display: block;
    width: 1040px;
    height: 576px;
  }
  .pattern-field { fill: var(--lavender); }
  .badge { fill: var(--violet); }
  .stamp-field { fill: var(--white); }
  .die-line {
    fill: none;
    stroke: var(--die-line);
    stroke-width: 2;
  }
  .brand-name {
    font-family: "Open Sans", sans-serif;
    font-weight: 400;
    fill: var(--white);
    letter-spacing: 1px;
  }
  .quote {
    font-family: "Dancing Script", cursive;
    font-weight: 500;
    font-size: 36px;
    fill: var(--quote-text);
  }
  .quote-author {
    font-family: "Open Sans", sans-serif;
    font-size: 17px;
    fill: var(--quote-text);
  }
</style>
</head>
<body>
<main class="sheet-stack">

  <!-- Außenseite: Rückseite links, Vorderseite rechts -->
  <svg class="sheet sheet-outside" viewBox="0 0 1040 576" aria-label="Außenseite der Probenverpackung">
    <rect class="pattern-field" x="0" y="0" width="1040" height="576" role="img" aria-label="Muster aus ineinander greifenden Kreisbögen in Lila"/>

    <g class="back-logo">
      <circle class="badge" cx="232" cy="187" r="98"/>
      <text class="brand-name" x="232" y="197" font-size="28" text-anchor="middle">RuchKontor</text>
    </g>

    <rect class="stamp-field" x="58" y="415" width="355" height="134" rx="32"/>

    <g class="front-logo">
      <circle class="badge" cx="806" cy="252" r="158"/>
      <text class="brand-name" x="806" y="268" font-size="46" text-anchor="middle">RuchKontor</text>
    </g>

    <g class="die-cut">
      <line class="die-line" x1="469" y1="0" x2="469" y2="576"/>
      <line class="die-line" x1="571" y1="0" x2="571" y2="576"/>
      <rect class="die-line" x="415" y="92" width="109" height="55"/>
      <rect class="die-line" x="368" y="248" width="199" height="78"/>
      <rect class="die-line" x="415" y="431" width="109" height="55"/>
    </g>
  </svg>

  <!-- Innenseite: Spruch links, Logo rechts -->
  <svg class="sheet sheet-inside" viewBox="0 0 1040 576" aria-label="Innenseite der Probenverpackung">
    <rect class="pattern-field" x="0" y="0" width="1040" height="576" role="img" aria-label="Muster aus ineinander greifenden Kreisbögen in Lila"/>

    <g class="quote-block">
      <circle class="badge" cx="208" cy="272" r="190"/>
      <text class="quote" text-anchor="middle">
        <tspan x="212" y="182">„Düfte sind wie</tspan>
        <tspan x="208" y="228">die Seele der Blumen,</tspan>
        <tspan x="208" y="274">man kann sie fühlen,</tspan>
        <tspan x="208" y="320">selbst im Reich der</tspan>
        <tspan x="208" y="366">Schatten.“</tspan>
      </text>
      <text class="quote-author" x="300" y="405" text-anchor="middle">Jules Marchand</text>
    </g>

    <g class="inside-logo">
      <circle class="badge" cx="855" cy="248" r="127"/>
      <text class="brand-name" x="855" y="261" font-size="37" text-anchor="middle">RuchKontor</text>
    </g>

    <g class="die-cut">
      <line class="die-line" x1="464" y1="0" x2="464" y2="576"/>
      <line class="die-line" x1="564" y1="0" x2="564" y2="576"/>
      <rect class="die-line" x="515" y="92" width="108" height="55"/>
      <rect class="die-line" x="466" y="248" width="204" height="78"/>
      <rect class="die-line" x="515" y="431" width="108" height="55"/>
    </g>
  </svg>

</main>
</body>
</html>
```